Tax consulting firm needs an advertisment for magazine/book/flyer

NEEDED
We need an advert to promote our general business with the following dimensions:-
230 x 148 + 5mm
PDF, 300 dpi
It is for inclusion in a larger publication - attached is the .pdf guide provided by the publisher with regard to dimensions needed.
The advert may also be used to print flyers in A5/A6 sizes so if it can also be scaled to fit those measurements that would be great.
BACKGROUND
We are a tax firm specialising in Luxembourg, UK and US personal taxes. We would like the advertisement to be in keeping with the feel of the website (www.morvelcount.com) and other material (winning files from previous design contests are attached for style/feel). The advert should be professional, modern, but elegant. Any photographs included should be in B&W and be of Luxembourg City and not of any other cities.
DETAILS
The design should utilise the colours of the brand:-
#7D1935
#4A96AD
#F5F3EE
The text "Specialists in Luxembourg, UK and US personal tax compliance and consulting" should be included and also website address and company logo.
For any questions, please send a message and I will respond as soon as I can.

```html
<!DOCTYPE html>
<html lang="en">
<head>
<meta charset="utf-8">
<title>Morvel Tax &amp; Consulting – Advertisement</title>
<link href="https://fonts.googleapis.com/css2?family=Kumbh+Sans:wght@400;700&display=swap" rel="stylesheet">
<style>
  :root {
    --maroon: #6A0A33;
    --teal: #4A96AD;
    --cream: #F5F3EE;
    --stage: #E9E6E0;
    --photo-sky: #C9CECE;
    --photo-mid: #8E8F8E;
    --photo-deep: #6C6C6C;
  }
  * { margin: 0; padding: 0; box-sizing: border-box; }
  html, body { width: 1200px; height: 900px; overflow: hidden; }
  body {
    background: var(--stage);
    font-family: "Kumbh Sans", "Century Gothic", sans-serif;
    position: relative;
  }
  .advert {
    position: absolute;
    width: 692px;
    height: 450px;
    background: var(--cream);
    overflow: hidden;
    box-shadow: 0 2px 10px rgba(0,0,0,0.18);
  }
  .advert--full { left: 58px; top: 66px; z-index: 2; }
  .advert--compact { left: 455px; top: 394px; z-index: 1; }

  .city-photo {
    position: absolute;
    left: 0; top: 0;
    width: 461px;
    height: 330px;
    background: linear-gradient(180deg,
      var(--photo-sky) 0%,
      var(--photo-mid) 40%,
      var(--photo-deep) 68%,
      var(--photo-mid) 84%,
      var(--cream) 100%);
  }
  .tagline {
    position: absolute;
    right: 258px;
    top: 311px;
    text-align: right;
    color: var(--maroon);
    font-weight: 700;
    font-size: 23px;
    letter-spacing: 0.6px;
    line-height: 27px;
    white-space: nowrap;
  }
  .brand-panel {
    position: absolute;
    right: 0; top: 0;
    width: 231px;
    height: 100%;
    background: var(--maroon);
  }
  .brand-mark {
    position: absolute;
    left: 33px;
    top: 60px;
    display: flex;
    align-items: center;
    gap: 8px;
    color: #fff;
  }
  .brand-mark__circle {
    width: 54px; height: 54px;
    border: 1.5px solid #fff;
    border-radius: 50%;
  }
  .brand-mark__name {
    font-weight: 400;
    font-size: 26px;
    line-height: 24px;
    letter-spacing: 0.5px;
  }
  .brand-mark__name small {
    display: block;
    font-size: 10.5px;
    line-height: 14px;
    letter-spacing: 0.3px;
  }
  .web-address {
    position: absolute;
    left: 22px;
    color: var(--teal);
    font-weight: 700;
    font-size: 16.5px;
    white-space: nowrap;
  }
  .advert--full .web-address { top: 297px; }
  .advert--compact .web-address { top: 121px; }
  .contact {
    position: absolute;
    right: 29px;
    top: 327px;
    text-align: right;
    color: var(--teal);
    font-size: 8.6px;
    line-height: 11px;
    white-space: nowrap;
  }
  .contact p + p { margin-top: 4px; }
</style>
</head>
<body>

  <section class="advert advert--full">
    <div class="city-photo" role="img" aria-label="Black and white photograph of historic Luxembourg City buildings with spires and towers"></div>
    <h2 class="tagline">Specialists in<br>Luxembourg, UK and US<br>personal tax compliance<br>and consulting</h2>
    <aside class="brand-panel">
      <div class="brand-mark">
        <span class="brand-mark__circle"></span>
        <span class="brand-mark__name">MORVEL<small>TAX &amp; CONSULTING</small></span>
      </div>
      <div class="web-address">www.morvelcount.com</div>
      <div class="contact">
        <p>Morvel S.à.r.l., 12, Rue des Prés,<br>Bergdorf, L-7420, Luxembourg</p>
        <p>Email: enquiries@morvelcount.com<br>Chat: morvel.tax</p>
        <p>Tel (Lux): +352 20 40 11 55<br>Tel (US): +1 555 010 2040<br>Tel (UK): +44 20 7946 0321</p>
      </div>
    </aside>
  </section>

  <section class="advert advert--compact">
    <div class="city-photo" role="img" aria-label="Black and white photograph of historic Luxembourg City buildings with spires and towers"></div>
    <h2 class="tagline">Specialists in<br>Luxembourg, UK and US<br>personal tax compliance<br>and consulting</h2>
    <aside class="brand-panel">
      <div class="brand-mark">
        <span class="brand-mark__circle"></span>
        <span class="brand-mark__name">MORVEL<small>TAX &amp; CONSULTING</small></span>
      </div>
      <div class="web-address">www.morvelcount.com</div>
    </aside>
  </section>

</body>
</html>
```